Präsentationsvorlagen für Unternehmensberater
Zielgruppe
Ich bin selbstständiger Unternehmensberater / Freelancer / Projektmanager / Interimmanager und Trainer in den Bereichen operative Logistik und Logistik-IT. Meine Kundenmix reicht vom Kleinunternehmen bis hin zu multinationalen Konzernen. Meine Projekte führen mich nach ganz Europa, mit Schwerpunkten im Osten. Als Projektsprachen verwende ich deutsch und englisch.
Aufgabenstellung
Ich suche nach einem umfangreichen Powerpoint-Masterfile zur Verwendung sowohl in der Aquisitionsphase als auch in den Projekten. Das moderne Design muss am Corporate Design angelehnt sein (siehe beiliegende Dateien, Webpage ist noch in Entwicklung, die aktuelle Layoutplanung ist aber verfügbar und kann bei Bedarf übermittelt werden). Geschwungene Formen bevorzuge ich gegenüber gradliniger Geometrie. Ein wenig verspielt darf es sein, ohne jedoch an Professionalität einzubüßen.
Folgendes soll im Masterfile berücksichtigt werden:
Aufbau:
- Dreistufige Struktur (Titel / Bereich / Thema)
- verborgene Folien / direkter Klick auf Themen z.B. von Inhaltsverzeichnis werden genutzt
- Animationen werden verwendet
- Seitenverhältnis 16:9
aktuell geplante Folientypen (Vorlage für alle Typen gewünscht):
- Agenda
- Übersicht / Inhalt
- Text/Aufzählung
- Zeitleiste
- Bilder mit/ohne Textspalte
- eingebundenes Video mit/ohne Text
- Darstellung ineinandergreifender Themen (ähnlich Puzzle)
- Diagramme (Kreisdiagramm, Balkendiagramm, Liniendiagramm, Spiderweb) jeweils mit und ohne Textspalte
- Gegenüberstellungen (z.B. Vor- und Nachteile)
- Wordcloud
- Prozessschritte
- Flowcharts
- Tabellen
- magisches Dreick/Vieleck (Darstellung untereinander konkurrierenden Ziele)
- Slogans / Zitate / Hypothesen
- Mengenüberschneidungen
- Call to Action
- Schlussfolie / Fragen?
- Kontaktdaten

```html
<!DOCTYPE html>
<html lang="de">
<head>
<meta charset="utf-8">
<title>velora – Präsentationsvorlage</title>
<link href="https://fonts.googleapis.com/css2?family=Poppins:wght@400;500;600;700&family=Roboto:wght@400;500;700&display=swap" rel="stylesheet">
<style>
:root{
  --blue:#3bb6e6;
  --blue-dark:#1a7fae;
  --blue-mid:#36b5e5;
  --blue-light:#8fd3f0;
  --blue-pale:#c4e8f7;
  --teal:#4a8f9c;
  --teal-dark:#2c5866;
  --brown:#3d3a33;
  --orange:#f07a3a;
  --ink:#1d1d1f;
  --grey:#8a8a8a;
  --line:#dcdcdc;
  --page:#f1f1f2;
  --violet:#7b6fe0;
}
*{box-sizing:border-box;margin:0;padding:0}
html,body{width:1200px;height:864px;overflow:hidden;background:var(--page)}
body{position:relative;font-family:'Roboto',sans-serif;color:var(--ink)}
.slide{position:absolute;width:346px;height:194px;background:#fff;overflow:hidden}
.slide *{position:absolute}
.c1{left:70px}.c2{left:435px}.c3{left:800px}
.r1{top:20px}.r2{top:232px}.r3{top:441px}.r4{top:655px}
.footer-line{left:15px;right:15px;top:180px;height:1px;background:var(--line)}
.footer{top:184px;font-size:3.6px;color:#9a9a9a;white-space:nowrap}
.f-date{left:16px}.f-web{left:0;right:0;text-align:center}.f-num{right:18px}
.dots{left:15px;top:155px;width:4px;height:20px}
.dots i{position:relative;display:block;width:3px;height:3px;border-radius:50%;background:var(--blue-dark);margin-bottom:5px}
.dots i:last-child{background:var(--blue-light)}
.brand{left:20px;top:7px;height:13px;display:flex;align-items:center;gap:3px}
.brand *{position:relative}
.brand-mark{width:13px;height:13px;border-radius:50%;border:2px solid var(--blue)}
.brand-text{line-height:1}
.brand-name{display:block;font-family:'Poppins',sans-serif;font-weight:600;font-size:9px;color:var(--blue);line-height:8px}
.brand-tag{display:block;font-size:2.2px;letter-spacing:.35px;color:#6b6b6b}
.title{font-family:'Poppins',sans-serif;font-weight:600;font-size:11.4px;letter-spacing:.1px;color:var(--ink);white-space:nowrap}
.body{font-size:3.6px;line-height:1.75;color:#7a7a7a}
.photo-office{background:linear-gradient(160deg,#dde7ef,#7d9fc0 55%,#2d4f7a)}
.photo-portrait{background:linear-gradient(160deg,#ece9e2,#d8d1c4 60%,#b7a994)}
.photo-team{background:linear-gradient(150deg,#5b6e4e,#8a7a63 40%,#4d6a86 75%,#8b4a4a)}
.photo-founder{background:linear-gradient(160deg,#e5ecf2,#9bb4c9)}
.art-target{background:linear-gradient(150deg,var(--blue-pale),var(--blue-mid) 55%,var(--blue-dark))}
/* slide 1 */
.social{top:15px;left:18px;display:flex;gap:13px;font-size:3.6px;color:#333}
.social span{position:relative}
.hero-brand{left:80px;top:69px;display:flex;align-items:center;gap:8px}
.hero-brand *{position:relative}
.hero-mark{width:48px;height:48px;border-radius:50%;border:5px solid var(--blue)}
.hero-name{display:block;font-family:'Poppins',sans-serif;font-weight:600;font-size:27px;line-height:26px;color:var(--blue)}
.hero-tag{display:block;font-size:7.2px;letter-spacing:1.6px;color:#555}
/* slide 2 */
.toc{left:18px;top:32px;width:311px;height:138px;background:var(--blue);color:#fff}
.toc-title{left:12px;top:13px;font-family:'Poppins',sans-serif;font-weight:600;font-size:11px}
.toc-row{font-size:4.6px;white-space:nowrap}
/* slide 3 */
.s-blue{background:var(--blue);color:#fff}
.s-blue .footer{color:#e6f6fd}
.s-blue .footer-line{background:rgba(255,255,255,.5)}
.s-blue .dots i{background:#fff}
.mark-white{left:9px;top:6px;width:32px;height:32px;border-radius:50%;border:3px solid #fff}
/* lists */
.num{width:11px;height:11px;border-radius:50%;border:1px solid #bbb;font-size:3.8px;font-weight:700;display:flex;align-items:center;justify-content:center;color:var(--ink)}
.item-title{font-size:4.6px;color:var(--blue)}
.icon-dot{width:17px;height:17px;border-radius:50%}
.pill{height:18px;width:100px;border-radius:9px;display:flex;align-items:center;font-family:'Poppins',sans-serif;font-weight:600;font-size:4px;color:#fff;padding-left:4px}
.pill *{position:relative}
.pill b{width:11px;height:11px;border-radius:50%;background:#fff;color:var(--ink);font-size:3.6px;display:flex;align-items:center;justify-content:center;margin-right:16px;border:1px solid #444}
.card{top:68px;width:59px;height:77px;color:#fff;text-align:center}
.card h4{position:relative;display:block;margin-top:29px;font-size:4.8px;font-weight:700;line-height:1.2}
.card p{position:relative;display:block;margin-top:5px;font-size:3.6px;line-height:1.75;padding:0 5px}
.card svg{left:24px;top:14px}
.ribbon{left:24px;width:66px;height:17px;display:flex;align-items:center;color:#fff;font-size:3.8px;font-weight:700;letter-spacing:.2px;padding-left:18px}
.ribbon svg{left:4px;top:4.5px}
</style>
</head>
<body>

<!-- 1 · Titel -->
<section class="slide c1 r1">
  <div class="social"><span>Netzwerk</span><span>Galerie</span><span>Kurznews</span></div>
  <div class="hero-brand">
    <span class="hero-mark"></span>
    <span><span class="hero-name">velora</span><span class="hero-tag">CONSULTING SERVICES</span></span>
  </div>
  <div class="dots"><i></i><i></i><i></i></div>
  <div class="footer-line"></div>
  <div class="footer f-date">17/02/2020</div><div class="footer f-web">www.velora-beratung.at</div><div class="footer f-num">#1</div>
</section>

<!-- 2 · Inhalt -->
<section class="slide c2 r1">
  <div class="brand"><span class="brand-mark"></span><span class="brand-text"><span class="brand-name">velora</span><span class="brand-tag">CONSULTING SERVICES</span></span></div>
  <div class="toc">
    <div class="toc-title">INHALT</div>
    <div class="toc-row" style="left:13px;top:38px">ÜBER UNS</div><div class="toc-row" style="left:104px;top:38px">05</div>
    <div class="toc-row" style="left:13px;top:50px">UNTERNEHMENSMILESTONES</div><div class="toc-row" style="left:104px;top:50px">06</div>
    <div class="toc-row" style="left:13px;top:62px">WORT VOM CEO</div><div class="toc-row" style="left:104px;top:62px">08</div>
    <div class="toc-row" style="left:13px;top:74px">UNSERE PHILOSOPHIE</div><div class="toc-row" style="left:104px;top:74px">10</div>
    <div class="toc-row" style="left:13px;top:86px">UNSER SERVICE</div><div class="toc-row" style="left:104px;top:86px">12</div>
    <div class="toc-row" style="left:13px;top:99px">UNSERE PREISE</div><div class="toc-row" style="left:104px;top:99px">14</div>
    <div class="toc-row" style="left:13px;top:111px">UNSER EINFACHER PROZESS</div><div class="toc-row" style="left:104px;top:111px">16</div>
    <div class="toc-row" style="left:13px;top:123px">FALLSTUDIE</div><div class="toc-row" style="left:104px;top:123px">18</div>
    <div class="toc-row" style="left:159px;top:38px">ERFOLGREICHES PROJEKT</div><div class="toc-row" style="left:266px;top:38px">20</div>
    <div class="toc-row" style="left:159px;top:50px">UNSERE ARBEIT</div><div class="toc-row" style="left:266px;top:50px">22</div>
    <div class="toc-row" style="left:159px;top:62px">UNSER KUNDE</div><div class="toc-row" style="left:266px;top:62px">30</div>
    <div class="toc-row" style="left:159px;top:74px">UNSER HAUSHALT</div><div class="toc-row" style="left:266px;top:74px">32</div>
    <div class="toc-row" style="left:159px;top:86px">PROJEKT ZEITLEISTE</div><div class="toc-row" style="left:266px;top:86px">34</div>
    <div class="toc-row" style="left:159px;top:99px">ALLGEMEINE GESCHÄFTSBEDINGUNGEN</div><div class="toc-row" style="left:266px;top:99px">35</div>
    <div class="toc-row" style="left:159px;top:111px">VERTRAGSVEREINBARUNG</div><div class="toc-row" style="left:266px;top:111px">36</div>
    <div class="toc-row" style="left:159px;top:123px">ABSCHLUSS VON</div><div class="toc-row" style="left:266px;top:123px">37</div>
  </div>
  <div class="footer-line"></div>
  <div class="footer f-date">17/02/2020</div><div class="footer f-web">www.velora-beratung.at</div><div class="footer f-num">#2</div>
</section>

<!-- 3 · Über uns -->
<section class="slide c3 r1 s-blue">
  <span class="mark-white"></span>
  <div class="title" style="left:38px;top:69px;color:#fff;font-size:10.6px">ÜBER UNS</div>
  <p class="body" style="left:38px;top:90px;width:160px;color:#eaf7fd">Lorem Ipsum is simply dummy text of the printing and typesetting industry. Lorem Ipsum has been the industry's standard dummy text ever since the 1500s, when an unknown printer took a galley of type and scrambled it to make a type specimen book. It has survived not only five centuries.</p>
  <div class="photo-portrait" role="img" aria-label="Foto: Beraterin am Laptop im Büro" style="left:218px;top:19px;width:109px;height:143px"></div>
  <div class="dots"><i></i><i></i><i></i></div>
  <div class="footer-line"></div>
  <div class="footer f-date">17/02/2020</div><div class="footer f-web">www.velora-beratung.at</div><div class="footer f-num">#3</div>
</section>

<!-- 4 · Gründer -->
<section class="slide c1 r2">
  <div class="title" style="left:0;right:0;top:13px;text-align:center">WILLKOMMEN DER GRÜNDER</div>
  <svg style="left:135px;top:34px" width="74" height="74" viewBox="0 0 74 74">
    <circle cx="37" cy="37" r="34" fill="none" stroke="var(--blue)" stroke-width="4"/>
    <circle cx="37" cy="37" r="29" fill="none" stroke="#555" stroke-width="3"/>
  </svg>
  <div class="photo-founder" role="img" aria-label="Porträtfoto des Gründers" style="left:144px;top:43px;width:56px;height:56px;border-radius:50%"></div>
  <div style="left:0;right:0;top:114px;text-align:center;font-family:'Poppins',sans-serif;font-size:4.8px;color:#333">Lena Hartwig</div>
  <div style="left:0;right:0;top:122px;text-align:center;font-size:3.4px;color:#888">Generaldirektor</div>
  <p class="body" style="left:50px;top:138px;width:246px;text-align:center">Lorem Ipsum is simply dummy text of the printing and typesetting industry. Lorem Ipsum has been the industry's standard dummy text ever since the 1500s, when an unknown printer took a galley of type and scrambled it to make a type specimen book. It has survived not only five centuries, but also the leap into electronic typesetting, remaining essentially unchanged.</p>
  <div class="dots"><i></i><i></i><i></i></div>
  <div class="footer-line"></div>
  <div class="footer f-date">17/02/2020</div><div class="footer f-web">www.velora-beratung.at</div><div class="footer f-num">#4</div>
</section>

<!-- 5 · Wer wir sind -->
<section class="slide c2 r2">
  <div class="brand"><span class="brand-mark"></span><span class="brand-text"><span class="brand-name">velora</span><span class="brand-tag">CONSULTING SERVICES</span></span></div>
  <div class="title" style="left:23px;top:53px">WER WIR SIND</div>
  <p class="body" style="left:23px;top:72px;width:88px;line-height:2.5">Lorem Ipsum is simply dummy text of the printing and typesetting industry. Lorem Ipsum has been the industry's standard dummy text ever since the 1500s, when an unknown printer took a galley of type and scrambled it to make a type specimen book. It has survived not only five centuries, but also the leap into electronic typesetting, remaining essentially unchanged.</p>
  <div class="photo-office" role="img" aria-label="Foto: Geschäftsleute im Gespräch am Fenster, Diagramme auf dem Tisch" style="left:116px;top:23px;width:95px;height:144px"></div>
  <span class="icon-dot" style="left:218px;top:51px;background:var(--blue-light)"></span>
  <span class="icon-dot" style="left:218px;top:90px;background:var(--teal-dark)"></span>
  <span class="icon-dot" style="left:218px;top:129px;background:var(--blue-light)"></span>
  <div style="left:244px;top:51px;font-size:4.6px;font-weight:700;color:#333">Wir sind hier um zu helfen</div>
  <p class="body" style="left:244px;top:58px;width:92px">Lorem Ipsum is simply dummy text of the printing and typesetting industry. Lorem Ipsum has been the industry's standard dummy.</p>
  <div style="left:244px;top:90px;font-size:4.6px;font-weight:700;color:#333">Wir machen Sie erfolgreich</div>
  <p class="body" style="left:244px;top:97px;width:92px">Lorem Ipsum is simply dummy text of the printing and typesetting industry. Lorem Ipsum has been the industry's standard dummy.</p>
  <div style="left:244px;top:129px;font-size:4.6px;font-weight:700;color:#333">Wir sind oben auf der Welt</div>
  <p class="body" style="left:244px;top:136px;width:92px">Lorem Ipsum is simply dummy text of the printing and typesetting industry. Lorem Ipsum has been the industry's standard dummy.</p>
  <div class="dots"><i></i><i></i><i></i></div>
  <div class="footer-line"></div>
  <div class="footer f-date">17/02/2020</div><div class="footer f-web">www.velora-beratung.at</div><div class="footer f-num">#5</div>
</section>

<!-- 6 · Was wir tun -->
<section class="slide c3 r2">
  <div class="brand"><span class="brand-mark"></span><span class="brand-text"><span class="brand-name">velora</span><span class="brand-tag">CONSULTING SERVICES</span></span></div>
  <div class="title" style="left:23px;top:49px">WAS WIR TUN</div>
  <div class="item-title" style="left:23px;top:68px">Year of 2017</div>
  <p class="body" style="left:23px;top:74px;width:120px">Sometimes the world looks perfect, nothing to rearrange. Sometimes you just, get a feeling like you need some kind</p>
  <div class="item-title" style="left:23px;top:96px">Year of 2018</div>
  <p class="body" style="left:23px;top:102px;width:120px">Sometimes the world looks perfect, nothing to rearrange. Sometimes you just, get a feeling like you need some kind</p>
  <div class="item-title" style="left:26px;top:126px">Year of 2019</div>
  <p class="body" style="left:26px;top:132px;width:120px">Sometimes the world looks perfect, nothing to rearrange. Sometimes you just, get a feeling like you need some kind</p>
  <div style="left:155px;top:70px;font-family:'Poppins',sans-serif;font-weight:600;font-size:9px;color:var(--blue)">85%</div>
  <div style="left:155px;top:105px;font-family:'Poppins',sans-serif;font-weight:600;font-size:9px;color:var(--blue)">89%</div>
  <div style="left:158px;top:136px;font-family:'Poppins',sans-serif;font-weight:600;font-size:9px;color:var(--blue)">90%</div>
  <div class="photo-team" role="img" aria-label="Foto von oben: Team arbeitet mit Laptops und Unterlagen am Holztisch" style="left:232px;top:0;width:114px;height:167px"></div>
  <div class="pill" style="left:193px;top:60px;background:var(--blue-pale);color:var(--ink)"><b>01</b>Lorem ipsum dolor sit amet</div>
  <div class="pill" style="left:193px;top:88px;background:var(--blue-dark)"><b>02</b>Lorem ipsum dolor sit amet</div>
  <div class="pill" style="left:193px;top:116px;background:var(--blue-mid)"><b>03</b>Lorem ipsum dolor sit amet</div>
  <div class="dots"><i></i><i></i><i></i></div>
  <div class="footer-line"></div>
  <div class="footer f-date">17/02/2020</div><div class="footer f-web">www.velora-beratung.at</div><div class="footer f-num">#5</div>
</section>

<!-- 7 · Unser Ziel -->
<section class="slide c1 r3">
  <div class="brand"><span class="brand-mark"></span><span class="brand-text"><span class="brand-name">velora</span><span class="brand-tag">CONSULTING SERVICES</span></span></div>
  <div class="title" style="left:174px;top:34px">UNSER ZIEL</div>
  <div class="art-target" role="img" aria-label="Illustration: Zielscheibe mit Pfeil in Blautönen" style="left:28px;top:52px;width:120px;height:125px"></div>
  <div class="num" style="left:174px;top:57px">01</div>
  <div class="item-title" style="left:195px;top:58px">Dein Titel hier</div>
  <p class="body" style="left:195px;top:68px;width:135px">Lorem Ipsum is simply dummy text of the printing and typesetting industry. Lorem Ipsum has been the industry's standard dummy text ever since the 1500s,</p>
  <div class="num" style="left:174px;top:97px">02</div>
  <div class="item-title" style="left:195px;top:98px">Dein Titel hier</div>
  <p class="body" style="left:195px;top:108px;width:135px">Lorem Ipsum is simply dummy text of the printing and typesetting industry. Lorem Ipsum has been the industry's standard dummy text ever since the 1500s,</p>
  <div class="num" style="left:174px;top:137px">03</div>
  <div class="item-title" style="left:195px;top:138px">Dein Titel hier</div>
  <p class="body" style="left:195px;top:148px;width:135px">Lorem Ipsum is simply dummy text of the printing and typesetting industry. Lorem Ipsum has been the industry's standard dummy text ever since the 1500s,</p>
  <div class="dots"><i></i><i></i><i></i></div>
  <div class="footer-line"></div>
  <div class="footer f-date">17/02/2020</div><div class="footer f-web">www.velora-beratung.at</div><div class="footer f-num">#6</div>
</section>

<!-- 8 · Warum uns wählen -->
<section class="slide c2 r3">
  <div class="brand"><span class="brand-mark"></span><span class="brand-text"><span class="brand-name">velora</span><span class="brand-tag">CONSULTING SERVICES</span></span></div>
  <div class="title" style="left:0;right:0;top:34px;text-align:center">WARUM UNS WÄHLEN ?</div>
  <div class="card" style="left:48px;background:var(--blue-dark)">
    <svg width="11" height="10" viewBox="0 0 11 10"><rect x="4" y="0" width="3" height="3" fill="#fff"/><rect x="0" y="7" width="3" height="3" fill="#fff"/><rect x="4" y="7" width="3" height="3" fill="#fff"/><rect x="8" y="7" width="3" height="3" fill="#fff"/><path d="M5.5 3v2M1.5 5h8v2M1.5 5v2M5.5 5v2" stroke="#fff" stroke-width=".7" fill="none"/></svg>
    <h4>Kann Client<br>erstellen</h4><p>Lorem Ipsum is simply dummy text of the printing and</p></div>
  <div class="card" style="left:112px;background:var(--blue-mid)">
    <svg width="11" height="10" viewBox="0 0 11 10"><circle cx="5.5" cy="3" r="2" fill="#fff"/><circle cx="1.8" cy="4" r="1.5" fill="#fff"/><circle cx="9.2" cy="4" r="1.5" fill="#fff"/><rect x="0" y="7" width="11" height="3" rx="1.5" fill="#fff"/></svg>
    <h4>Unterstützt von<br>Processional</h4><p>Lorem Ipsum is simply dummy text of the printing and</p></div>
  <div class="card" style="left:176px;background:var(--blue-light);color:var(--ink)">
    <svg width="11" height="10" viewBox="0 0 11 10"><circle cx="5.5" cy="2.5" r="2.5" fill="var(--ink)"/><path d="M2 10 L4 5 H7 L9 10Z" fill="var(--ink)"/></svg>
    <h4>Produkt<br>garantie</h4><p>Lorem Ipsum is simply dummy text of the printing and</p></div>
  <div class="card" style="left:240px;background:var(--blue-pale);color:var(--ink)">
    <svg width="11" height="10" viewBox="0 0 11 10"><circle cx="2.5" cy="1.5" r="1.5" fill="var(--ink)"/><circle cx="8.5" cy="1.5" r="1.5" fill="var(--ink)"/><rect x="1" y="3.5" width="3" height="6.5" fill="var(--ink)"/><rect x="7" y="3.5" width="3" height="6.5" fill="var(--ink)"/></svg>
    <h4>Kostenlose<br>Beratung</h4><p>Lorem Ipsum is simply dummy text of the printing and</p></div>
  <div class="dots"><i></i><i></i><i></i></div>
  <div class="footer-line"></div>
  <div class="footer f-date">17/02/2020</div><div class="footer f-web">www.velora-beratung.at</div><div class="footer f-num">#7</div>
</section>

<!-- 9 · Marketing Strategien -->
<section class="slide c3 r3">
  <div class="brand"><span class="brand-mark"></span><span class="brand-text"><span class="brand-name">velora</span><span class="brand-tag">CONSULTING SERVICES</span></span></div>
  <div style="left:32px;top:35px;width:6px;height:143px;background:#d4d4d4"></div>
  <div class="ribbon" style="top:41px;background:var(--blue-mid)"><svg width="5" height="5" viewBox="0 0 10 10"><circle cx="5" cy="5" r="5" fill="#fff"/><path d="M2.5 5l2 2 3-4" stroke="var(--blue-mid)" stroke-width="1.5" fill="none"/></svg>HIER UNTERTITEL</div>
  <div class="ribbon" style="top:70px;background:var(--teal-dark)"><svg width="5" height="5" viewBox="0 0 10 10"><circle cx="5" cy="5" r="5" fill="#fff"/><path d="M2.5 5l2 2 3-4" stroke="var(--teal-dark)" stroke-width="1.5" fill="none"/></svg>HIER UNTERTITEL</div>
  <div class="ribbon" style="top:100px;background:var(--brown)"><svg width="5" height="5" viewBox="0 0 10 10"><circle cx="5" cy="5" r="5" fill="#fff"/><path d="M2.5 5l2 2 3-4" stroke="var(--brown)" stroke-width="1.5" fill="none"/></svg>HIER UNTERTITEL</div>
  <div class="ribbon" style="top:129px;background:var(--orange)"><svg width="5" height="5" viewBox="0 0 10 10"><circle cx="5" cy="5" r="5" fill="#fff"/><path d="M2.5 5l2 2 3-4" stroke="var(--orange)" stroke-width="1.5" fill="none"/></svg>HIER UNTERTITEL</div>
  <div class="title" style="left:154px;top:34px">MARKETING STRATEGIEN</div>
  <div style="left:230px;top:67px;width:1px;height:104px;background:#333"></div>
  <div style="left:149px;top:118px;width:160px;height:1px;background:#333"></div>
  <span class="icon-dot" style="left:152px;top:78px;background:var(--blue-mid)"></span>
  <span class="icon-dot" style="left:237px;top:78px;background:var(--ink)"></span>
  <span class="icon-dot" style="left:152px;top:129px;background:var(--teal-dark)"></span>
  <span class="icon-dot" style="left:237px;top:129px;background:var(--orange)"></span>
  <p class="body" style="left:152px;top:98px;width:70px;font-size:3.2px">Lorem ipsum dolor sit amet, consectetur adipiscing elit, sed do eiusmod quis.</p>
  <p class="body" style="left:239px;top:98px;width:70px;font-size:3.2px">Lorem ipsum dolor sit amet, consectetur adipiscing elit, sed do eiusmod quis.</p>
  <p class="body" style="left:152px;top:148px;width:70px;font-size:3.2px">Lorem ipsum dolor sit amet, consectetur adipiscing elit, sed do eiusmod quis</p>
  <p class="body" style="left:239px;top:148px;width:70px;font-size:3.2px">Lorem ipsum dolor sit amet, consectetur adipiscing elit, sed do eiusmod quis</p>
  <div class="dots"><i></i><i></i><i></i></div>
  <div class="footer-line"></div>
  <div class="footer f-date">17/02/2020</div><div class="footer f-web">www.velora-beratung.at</div><div class="footer f-num">#8</div>
</section>

<!-- 10 · Geschäftsplaner -->
<section class="slide c1 r4">
  <div class="brand"><span class="brand-mark"></span><span class="brand-text"><span class="brand-name">velora</span><span class="brand-tag">CONSULTING SERVICES</span></span></div>
  <div class="title" style="left:118px;top:29px;font-size:10.6px">GESCHÄFTSPLANER</div>
  <svg style="left:26px;top:48px" width="128" height="130" viewBox="0 0 128 130">
    <circle cx="64" cy="64" r="59" fill="#f0f0f0"/>
    <circle cx="64" cy="64" r="41" fill="#e1e1e1"/>
    <circle cx="64" cy="64" r="33" fill="#ebebeb"/>
    <path d="M64 64 L64 0 A64 64 0 0 1 109.3 18.7Z" fill="var(--blue-light)"/>
    <path d="M64 64 L109.3 18.7 A64 64 0 0 1 128 64Z" fill="var(--teal)"/>
    <path d="M64 64 L128 64 A64 64 0 0 1 109.3 109.3Z" fill="#efece6"/>
    <path d="M64 64 L109.3 109.3 A64 64 0 0 1 64 128Z" fill="var(--orange)"/>
    <circle cx="64" cy="64" r="20" fill="#fff"/>
    <text x="64" y="65.5" font-family="Poppins, sans-serif" font-weight="600" font-size="4" text-anchor="middle" fill="#333">PIE CHART</text>
    <circle cx="82" cy="24" r="3.5" fill="none" stroke="#fff" stroke-width="1"/>
    <path d="M94 46 l9-4 -4 9 -1-4z" fill="#fff"/>
    <ellipse cx="99" cy="79" rx="5" ry="3" fill="#fff"/>
    <path d="M81 100 v9 l7-4.5z" fill="#fff"/>
  </svg>
  <p class="body" style="left:142px;top:49px;width:175px;font-size:3.8px;color:var(--blue)">Lorem ipsum dolor sit amet, conse ctetur adipis cing elit sed do eiusmod lorem ipsum Lorem ipsum dolor</p>
  <p class="body" style="left:168px;top:82px;width:160px;font-size:3.8px;color:var(--blue)">Lorem ipsum dolor sit amet, conse ctetur adipis cing elit sed do eiusmod lorem ipsum Lorem ipsum dolor</p>
  <p class="body" style="left:162px;top:129px;width:160px;font-size:3.8px;color:#777">Lorem ipsum dolor sit amet, conse ctetur adipis cing elit sed do eiusmod lorem ipsum Lorem ipsum dolor</p>
  <p class="body" style="left:142px;top:159px;width:175px;font-size:3.8px;color:var(--orange)">Lorem ipsum dolor sit amet, conse ctetur adipis cing elit sed do eiusmod lorem ipsum Lorem ipsum dolor</p>
  <div class="dots"><i></i><i></i><i></i></div>
  <div class="footer-line"></div>
  <div class="footer f-date">17/02/2020</div><div class="footer f-web">www.velora-beratung.at</div><div class="footer f-num">#9</div>
</section>

<!-- 11 · Balkendiagramm -->
<section class="slide c2 r4">
  <div class="brand"><span class="brand-mark"></span><span class="brand-text"><span class="brand-name">velora</span><span class="brand-tag">CONSULTING SERVICES</span></span></div>
  <div class="title" style="left:19px;top:62px;font-size:10.6px">Block text</div>
  <p class="body" style="left:19px;top:83px;width:118px;line-height:2.4">Lorem ipsum dolor sit amet, consecr adipiscing elit, sed do eiusmod tempr incididunt ut labore et dolore magna aliqua. Ut enim ad exercitation ullamo</p>
  <svg style="left:150px;top:26px" width="190" height="145" viewBox="0 0 190 145" font-family="Roboto, sans-serif" font-size="5.5" fill="#333">
    <defs>
      <linearGradient id="barTop" x1="0" y1="1" x2="0" y2="0"><stop offset="0" stop-color="#fff"/><stop offset="1" stop-color="var(--violet)"/></linearGradient>
    </defs>
    <g stroke="#bfe6f6" stroke-width=".6">
      <line x1="20" y1="126" x2="183" y2="126"/><line x1="20" y1="114" x2="183" y2="114"/><line x1="20" y1="102" x2="183" y2="102"/><line x1="20" y1="90" x2="183" y2="90"/><line x1="20" y1="78" x2="183" y2="78"/><line x1="20" y1="66" x2="183" y2="66"/><line x1="20" y1="54" x2="183" y2="54"/><line x1="20" y1="42" x2="183" y2="42"/><line x1="20" y1="30" x2="183" y2="30"/><line x1="20" y1="18" x2="183" y2="18"/><line x1="20" y1="6" x2="183" y2="6"/>
    </g>
    <g text-anchor="end"><text x="14" y="128">0</text><text x="14" y="116">1</text><text x="14" y="104">2</text><text x="14" y="92">3</text><text x="14" y="80">4</text><text x="14" y="68">5</text><text x="14" y="56">6</text><text x="14" y="44">7</text><text x="14" y="32">8</text><text x="14" y="20">9</text><text x="14" y="8">10</text></g>
    <rect x="36" y="74" width="22" height="52" fill="var(--blue-light)"/><rect x="36" y="45.6" width="22" height="28.4" fill="var(--teal)"/><rect x="36" y="21.6" width="22" height="24" fill="url(#barTop)"/>
    <rect x="91" y="97" width="21" height="29" fill="var(--blue-light)"/><rect x="91" y="43" width="21" height="54" fill="var(--teal)"/><rect x="91" y="19" width="21" height="24" fill="url(#barTop)"/>
    <rect x="146" y="84" width="21" height="42" fill="var(--blue-light)"/><rect x="146" y="62.4" width="21" height="21.6" fill="var(--teal)"/><rect x="146" y="26.4" width="21" height="36" fill="url(#barTop)"/>
    <g text-anchor="middle"><text x="47" y="141">Step1</text><text x="101.5" y="141">Step2</text><text x="156.5" y="141">Step3</text></g>
  </svg>
  <div class="dots"><i></i><i></i><i></i></div>
  <div class="footer-line"></div>
  <div class="footer f-date">17/02/2020</div><div class="footer f-web">www.velora-beratung.at</div><div class="footer f-num">#10</div>
</section>

<!-- 12 · Horizontales Diagramm -->
<section class="slide c3 r4">
  <div class="brand"><span class="brand-mark"></span><span class="brand-text"><span class="brand-name">velora</span><span class="brand-tag">CONSULTING SERVICES</span></span></div>
  <div class="title" style="left:0;right:0;top:31px;text-align:center;font-size:10.6px">Chart Title</div>
  <svg style="left:36px;top:50px" width="280" height="88" viewBox="0 0 280 88" font-family="Roboto, sans-serif" font-size="5.5" fill="#333">
    <defs>
      <linearGradient id="barEnd" x1="0" y1="0" x2="1" y2="0"><stop offset="0" stop-color="#fff"/><stop offset="1" stop-color="var(--violet)"/></linearGradient>
    </defs>
    <g stroke="#bfe6f6" stroke-width=".6">
      <line x1="41.7" y1="2" x2="41.7" y2="73"/><line x1="79.4" y1="2" x2="79.4" y2="73"/><line x1="117.2" y1="2" x2="117.2" y2="73"/><line x1="154.9" y1="2" x2="154.9" y2="73"/><line x1="192.6" y1="2" x2="192.6" y2="73"/><line x1="230.3" y1="2" x2="230.3" y2="73"/><line x1="268" y1="2" x2="268" y2="73"/>
    </g>
    <rect x="4" y="8" width="85" height="4" fill="var(--blue-light)"/><rect x="89" y="8" width="53" height="4" fill="var(--teal)"/><rect x="142" y="8" width="94" height="4" fill="url(#barEnd)"/>
    <rect x="4" y="26" width="66" height="4" fill="var(--blue-light)"/><rect x="70" y="26" width="34" height="4" fill="var(--teal)"/><rect x="104" y="26" width="56" height="4" fill="url(#barEnd)"/>
    <rect x="4" y="43" width="47" height="4" fill="var(--blue-light)"/><rect x="51" y="43" width="85" height="4" fill="var(--teal)"/><rect x="136" y="43" width="36" height="4" fill="url(#barEnd)"/>
    <rect x="4" y="61" width="81" height="4" fill="var(--blue-light)"/><rect x="85" y="61" width="47" height="4" fill="var(--teal)"/><rect x="132" y="61" width="36" height="4" fill="url(#barEnd)"/>
    <g text-anchor="middle"><text x="4" y="83">0</text><text x="41.7" y="83">2</text><text x="79.4" y="83">4</text><text x="117.2" y="83">6</text><text x="154.9" y="83">8</text><text x="192.6" y="83">10</text><text x="230.3" y="83">12</text><text x="268" y="83">14</text></g>
  </svg>
  <p class="body" style="left:40px;right:40px;top:148px;text-align:center;font-size:3.8px;line-height:3">Lorem ipsum dolor sit amet, consecr adipiscing elit, sed do eiusmod tempr incididunt ut labore et dolore magna aliqua. Ut enim ad exercitation ullamo.</p>
  <div class="dots"><i></i><i></i><i></i></div>
  <div class="footer-line"></div>
  <div class="footer f-date">17/02/2020</div><div class="footer f-web">www.velora-beratung.at</div><div class="footer f-num">#10</div>
</section>

</body>
</html>
```